Delvane Advisory Partners
Simple
Dr. Paul Merideth
347 Brookfield Lane
Los Altos, CA 94024
mtorvell@delvaneadvisorypartners.example
www.delvaneadvisorypartners.example
I wish to create a classy, simple, elegant single-sided business card for my consulting company.
I only wish for my number, e-mail, and website information to be on the card, NOT my address. Also, no need to put "cell" or "e-mail" or "web" on the card, just the information.

```html
<!DOCTYPE html>
<html lang="en">
<head>
<meta charset="utf-8">
<title>Delvane Advisory Partners — Stationery Set</title>
<link rel="stylesheet" href="https://fonts.googleapis.com/css2?family=Cinzel:wght@600&family=Open+Sans:wght@400;600&display=swap">
<style>
  :root {
    --backdrop: #e8e3da;
    --paper: #ffffff;
    --ink: #2a2a2a;
    --ink-soft: #6a6a6a;
    --band: #262626;
    --rule: #9a9a9a;
    --label: #3b3b3b;
  }
  * { box-sizing: border-box; margin: 0; padding: 0; }
  html, body { width: 1200px; height: 562px; overflow: hidden; }
  body {
    background: var(--backdrop);
    font-family: "Open Sans", Arial, sans-serif;
    color: var(--ink);
    position: relative;
  }
  .piece { position: absolute; background: var(--paper); box-shadow: 0 2px 6px rgba(0,0,0,.25); }
  .piece-label {
    position: absolute; top: -14px; left: 0; right: 0; text-align: center;
    font-size: 8px; color: var(--label);
  }
  .brand-name {
    font-family: "Cinzel", Georgia, serif; font-weight: 600; color: var(--ink);
    text-transform: uppercase; letter-spacing: .06em; line-height: 1.05;
  }
  .brand-name .sub { display: block; font-size: .42em; letter-spacing: .18em; }
  .edge-band { position: absolute; left: 0; top: 0; bottom: 0; width: 10px; background: var(--band); }

  /* Fax cover */
  .fax-cover { left: 36px; top: 19px; width: 355px; height: 514px; }
  .fax-cover .brand-name { position: absolute; left: 24px; top: 18px; font-size: 27px; }
  .fax-title { position: absolute; right: 14px; top: 48px; font-size: 9px; font-weight: 600; letter-spacing: .1em; }
  .fax-table { position: absolute; left: 22px; right: 12px; top: 60px; border-top: 3px solid var(--band); }
  .fax-row { display: flex; border-bottom: 1px solid var(--rule); height: 16px; }
  .fax-cell { flex: 1; font-size: 6px; padding: 4px 0 0 4px; border-left: 1px solid var(--rule); }
  .fax-cell:first-child { border-left: none; }
  .fax-checks { position: absolute; left: 26px; top: 138px; display: flex; gap: 16px; font-size: 5.5px; }
  .fax-checks span::before { content: ""; display: inline-block; width: 6px; height: 6px; border: 1px solid var(--ink-soft); margin-right: 4px; vertical-align: -1px; }
  .footer-line { position: absolute; left: 22px; right: 12px; bottom: 14px; font-size: 4.6px; color: var(--ink-soft); display: flex; gap: 12px; }

  /* Letterhead */
  .letterhead { left: 413px; top: 19px; width: 355px; height: 514px; }
  .letterhead .brand-name { position: absolute; left: 0; right: 0; top: 18px; text-align: center; font-size: 27px; }

  /* Business cards */
  .card { top: 19px; width: 140px; height: 78px; }
  .card-front { left: 773px; background: var(--band); color: #fff; }
  .card-front .brand-name { position: absolute; left: 10px; top: 14px; font-size: 9px; color: #fff; }
  .card-details { position: absolute; right: 10px; top: 40px; text-align: left; font-size: 4.4px; line-height: 1.5; color: #e6e6e6; }
  .card-details .name { font-weight: 600; font-size: 5px; }
  .card-back { left: 931px; }
  .card-back .brand-name { position: absolute; left: 0; right: 0; top: 26px; text-align: center; font-size: 14px; }

  /* Envelopes */
  .envelope-front { left: 773px; top: 132px; width: 296px; height: 137px; }
  .envelope-front .brand-name { position: absolute; left: 22px; top: 12px; font-size: 17px; }
  .return-address { position: absolute; left: 22px; top: 46px; font-size: 4.6px; color: var(--ink-soft); }
  .envelope-back { left: 773px; top: 384px; width: 296px; height: 140px; }
  .envelope-back svg { position: absolute; inset: 0; }
  .envelope-back .brand-name { position: absolute; left: 0; right: 0; top: 30px; text-align: center; font-size: 17px; }
</style>
</head>
<body>

<section class="piece fax-cover">
  <p class="piece-label">Fax Cover</p>
  <div class="edge-band"></div>
  <h1 class="brand-name">Delvane<span class="sub">Advisory Partners</span></h1>
  <p class="fax-title">FAX</p>
  <div class="fax-table">
    <div class="fax-row"><div class="fax-cell">To:</div><div class="fax-cell">From:</div></div>
    <div class="fax-row"><div class="fax-cell">Fax:</div><div class="fax-cell">Pages:</div></div>
    <div class="fax-row"><div class="fax-cell">Phone:</div><div class="fax-cell">Date:</div></div>
    <div class="fax-row"><div class="fax-cell">Re:</div><div class="fax-cell">CC:</div></div>
  </div>
  <div class="fax-checks">
    <span>Urgent</span><span>For Review</span><span>Please Comment</span><span>Please Reply</span><span>Please Recycle</span>
  </div>
  <p class="footer-line"><span>347 Brookfield Lane, Los Altos, CA 94024</span><span>(650) 555-0148</span><span>mtorvell@delvaneadvisorypartners.example</span></p>
</section>

<section class="piece letterhead">
  <p class="piece-label">Letterhead</p>
  <div class="edge-band"></div>
  <h1 class="brand-name">Delvane<span class="sub">Advisory Partners</span></h1>
  <p class="footer-line"><span>347 Brookfield Lane, Los Altos, CA 94024</span><span>(650) 555-0148</span><span>mtorvell@delvaneadvisorypartners.example</span></p>
</section>

<section class="piece card card-front">
  <p class="piece-label">Business Card (Front)</p>
  <h2 class="brand-name">Delvane<span class="sub">Advisory Partners</span></h2>
  <div class="card-details">
    <p class="name">Dr. Paul Merideth</p>
    <p>Principal Consultant</p>
    <p>(650) 555-0148</p>
    <p>mtorvell@delvaneadvisorypartners.example</p>
    <p>www.delvaneadvisorypartners.example</p>
  </div>
</section>

<section class="piece card card-back">
  <p class="piece-label">Business Card (Back)</p>
  <h2 class="brand-name">Delvane<span class="sub">Advisory Partners</span></h2>
</section>

<section class="piece envelope-front">
  <p class="piece-label">Envelope (Front)</p>
  <div class="edge-band"></div>
  <h2 class="brand-name">Delvane<span class="sub">Advisory Partners</span></h2>
  <p class="return-address">347 Brookfield Lane, Los Altos, CA 94024</p>
</section>

<section class="piece envelope-back">
  <p class="piece-label">Envelope (Back)</p>
  <svg width="296" height="140" viewBox="0 0 296 140" aria-hidden="true">
    <path d="M0 0 L148 92 L296 0" fill="none" stroke="#b5b5b5" stroke-width="1"/>
  </svg>
  <h2 class="brand-name">Delvane<span class="sub">Advisory Partners</span></h2>
</section>

</body>
</html>
```